TK AG Flyer design

I’d like to redesign an A5, double-sided flyer for the company TK AG (www.tkag.lu). The text/content is available in a Word document.

```html
<!DOCTYPE html>
<html lang="de">
<head>
<meta charset="utf-8">
<title>TK AG – Flyer A5</title>
<link href="https://fonts.googleapis.com/css2?family=Arimo:wght@400;700&display=swap" rel="stylesheet">
<style>
  :root{
    --navy:#2b2d7c;
    --amber:#eaab43;
    --orange:#e9993a;
    --white:#ffffff;
    --stage:#000000;
    --sky-top:#5f8fd6;
    --sky-bottom:#b9cde8;
  }
  *{margin:0;padding:0;box-sizing:border-box}
  html,body{width:1200px;height:850px;overflow:hidden;background:var(--stage)}
  body{position:relative;font-family:"Arimo",Arial,sans-serif;color:var(--navy)}
  .page{position:absolute;width:546px;height:774px;background:var(--white);overflow:hidden}
  .page--front{left:36px;top:36px}
  .page--back{left:609px;top:38px}
  .photo{position:absolute;left:0;top:0;width:100%;height:149px}
  .photo--front{background:linear-gradient(160deg,var(--sky-top),#2c4f9c 45%,var(--sky-bottom))}
  .photo--back{background:linear-gradient(200deg,#8fb2e0,#2e4a8f 50%,#6d5a4a)}
  .headline{position:absolute;left:0;width:100%;text-align:center;font-weight:700;font-size:27px;line-height:34px;letter-spacing:-0.4px}
  .headline span{background:linear-gradient(transparent 52%,var(--amber) 52%,var(--amber) 88%,transparent 88%);padding:0 2px}
  .front-headline{top:156px}
  .back-headline{top:160px}
  .intro{position:absolute;top:228px;left:0;width:100%;text-align:center;font-size:12.5px;line-height:16px}
  .service{position:absolute;top:307px;width:227px;height:243px;background:var(--amber);border-radius:16px;padding:18px 15px 0}
  .service--solar{left:37px}
  .service--efficiency{left:282px}
  .service-icon{position:absolute;top:-25px;left:50%;margin-left:-21px;width:42px;height:42px;border-radius:50%;background:var(--navy);display:flex;align-items:center;justify-content:center}
  .service-title{color:var(--white);font-weight:700;font-size:18.5px;margin-bottom:4px}
  .service-lead{font-weight:700;font-size:12.8px;line-height:15.5px;margin-bottom:3px}
  .service-list{list-style:none;font-size:12.5px;line-height:15.5px}
  .service-list li{position:relative;padding-left:18px;margin-bottom:2px}
  .service-list li::before{content:"";position:absolute;left:7px;top:6px;width:5px;height:5px;border-radius:50%;background:var(--navy)}
  .service-list b{font-weight:700}
  .contact-badge{position:absolute;left:203px;top:519px;width:140px;height:140px;border-radius:50%;background:var(--navy);display:flex;flex-direction:column;align-items:center;justify-content:center;text-align:center}
  .contact-badge-inner{transform:rotate(-12deg);line-height:1.2}
  .contact-cta{color:var(--amber);font-weight:700;font-size:11.5px}
  .contact-phone{color:var(--amber);font-weight:700;font-size:20px;margin:3px 0}
  .contact-mail{color:var(--amber);font-size:11.5px}
  .brand{position:absolute;top:694px;left:0;width:100%;display:flex;align-items:center;justify-content:center;gap:12px}
  .brand-dot{width:22px;height:22px;border-radius:50%;background:var(--amber)}
  .brand-name{font-weight:400;font-size:30px;color:var(--navy);letter-spacing:1px}
  .pv-option{position:absolute;top:234px;font-size:12.5px;line-height:15.7px;text-align:justify}
  .pv-option--indach{left:37px;width:228px}
  .pv-option--aufdach{left:293px;width:219px}
  .pv-option svg{display:block;margin-bottom:2px}
  .topic{position:absolute;left:37px;width:236px;font-size:12.5px;line-height:15.7px;text-align:justify}
  .topic h3{color:var(--orange);font-size:15.5px;line-height:18.5px;font-weight:700;text-align:left;margin-bottom:2px}
  .topic--consumption{top:356px}
  .topic--renovation{top:525px}
  .process{position:absolute;left:293px;top:388px;width:219px;height:223px;border-radius:12px;background:linear-gradient(45deg,var(--amber),#f6dcac 70%,#fbeedb);padding:14px 11px}
  .process h4{font-size:12.8px;font-weight:700;margin-bottom:7px}
  .process ol{list-style:none;font-size:12.5px;line-height:15.7px}
  .process li{position:relative;padding-left:15px;margin-bottom:3px}
  .process li span{position:absolute;left:0;font-weight:700}
  .footer{position:absolute;left:0;top:675px;width:100%;height:99px;background:var(--navy);color:var(--white);font-size:11.8px;line-height:14px}
  .footer-address{position:absolute;left:37px;top:14px}
  .footer-group{position:absolute;left:293px;top:14px}
  .footer strong{color:var(--amber);font-size:13px}
  .footer .accent{color:var(--amber)}
</style>
</head>
<body>

<section class="page page--front">
  <div class="photo photo--front" role="img" aria-label="Foto: Techniker mit Helm prüft Solarmodule auf einem Dach unter blauem Himmel"></div>
  <h1 class="headline front-headline"><span>Mehr Eigenverbrauch.</span><br><span>Mehr Effizienz. Mehr Zukunft.</span></h1>
  <p class="intro">Wir planen und beraten rund um Photovoltaik und Energieeffizienz –<br>für <b>Private, Gewerbe und Industrie.</b></p>

  <div class="service service--solar">
    <div class="service-icon">
      <svg width="24" height="20" viewBox="0 0 24 20" fill="none" stroke="#fff" stroke-width="1.3"><path d="M4 2h16l3 12H1z"/><path d="M3 6h18M2 10h20M8.5 2 7 14M15.5 2 17 14M12 14v4M8 18h8"/></svg>
    </div>
    <h2 class="service-title">Solar Energie</h2>
    <p class="service-lead">Photovoltaik-Lösungen,<br>die zu Ihrem Dach passen</p>
    <ul class="service-list">
      <li><b>Indach PV-Anlagen</b><br>(integriert &amp; ästhetisch)</li>
      <li><b>Aufdach PV-Anlagen</b><br>(effizient &amp; preis-/<br>leistungsstark)</li>
      <li><b>Eigenverbrauch optimieren</b><br>(BaFerie, Wärmepumpe,<br>E-Mobility, smartes<br>Lastmanagement)</li>
    </ul>
  </div>

  <div class="service service--efficiency">
    <div class="service-icon">
      <svg width="22" height="20" viewBox="0 0 22 20"><path d="M11 1 1 9h3v10h14V9h3z" fill="var(--amber)"/><path d="M12 6l-4 6h3l-1 5 4-6h-3z" fill="#fff"/></svg>
    </div>
    <h2 class="service-title">Energie Effizienz</h2>
    <p class="service-lead">Beratung &amp; Konzepte für<br>nachhaltige Gebäude</p>
    <ul class="service-list">
      <li><b>Energieberatung / GEAK /<br>GEAK Plus</b></li>
      <li><b>Impulsberatung &amp;<br>Energiekonzept</b> (HLK + PV,<br>Simulationen, Nachweise)</li>
      <li><b>Energiesanierung</b><br>(Planung, Koordination,<br>Förderabwicklung)</li>
    </ul>
  </div>

  <div class="contact-badge">
    <div class="contact-badge-inner">
      <div class="contact-cta">Jetzt unverbindlich<br>Kontakt aufnehmen</div>
      <div class="contact-phone">XX XXX XX</div>
      <div class="contact-mail">tkluzern@de</div>
    </div>
  </div>

  <div class="brand">
    <div class="brand-dot"></div>
    <div class="brand-name">TK AG</div>
  </div>
</section>

<section class="page page--back">
  <div class="photo photo--back" role="img" aria-label="Foto: Schrägdach mit Solarmodulen und Kamin vor blauem Himmel"></div>
  <h1 class="headline back-headline"><span>Indach oder Aufdach?</span><br><span>Wir finden die passende Lösung.</span></h1>

  <div class="pv-option pv-option--indach">
    <svg width="34" height="32" viewBox="0 0 34 32" fill="none" stroke="var(--navy)" stroke-width="1.6"><circle cx="17" cy="5" r="2.5" stroke="var(--amber)"/><path d="M4 14h26l3 16H1z M2.5 20h29M2 25h30M10 14 8.5 30M17 14v16M24 14l1.5 16"/></svg>
    <b>Indach PV</b> ist ideal bei Neubau oder Dachsanierung: Module ersetzen die Dacheindeckung – funktional und optisch hochwertig.
  </div>
  <div class="pv-option pv-option--aufdach">
    <svg width="40" height="32" viewBox="0 0 40 32" fill="none" stroke="var(--navy)" stroke-width="1.6"><circle cx="6" cy="4" r="2.5" stroke="var(--amber)"/><path d="M8 30 16 10h12l-8 20zM28 10l10 20H20M11 22h13M13.5 16h12"/></svg>
    <b>Aufdach PV</b> eignet sich besonders bei bestehenden Dächern in gutem Zustand – mit Standardmodulen oft die effizienteste Technologie zum besten Preis.
  </div>

  <div class="topic topic--consumption">
    <h3>Eigenverbrauch erhöhen –<br>Rendite steigern</h3>
    Viele PV-Anlagen produzieren mehr Strom, als gleichzeitig benötigt wird. Mit passenden Massnahmen erhöhen Sie Ihren Eigenverbrauch – z. B. durch <b>BaZeriesysteme, Wärmepumpen-Ansteuerung, überschussvariables Laden von E-Fahrzeugen</b> oder gezieltes Schalten von Verbrauchern.
  </div>
  <div class="topic topic--renovation">
    <h3>Energieberatung &amp; Sanierung –<br>ganzheitlich gedacht</h3>
    Wir analysieren Ihr Gebäude, erstellen einen <b>Sanierungs-und Effizienzplan</b> und unterstützen bei Bewilligungen und Fördergeldern – bis zur Umsetzung und Abnahme.
  </div>

  <div class="process">
    <h4>So läuft die Zusammenarbeit</h4>
    <ol>
      <li><span>1.</span>Erstkontakt (Telefon/E-Mail)</li>
      <li><span>2.</span>Analyse / Check vor Ort<br>(Daten, Bedarf, Potenziale)</li>
      <li><span>3.</span>Konzept, WirtschaBlichkeit &amp;<br>Massnahmenplan</li>
      <li><span>4.</span>Umsetzung mit eingespieltem<br>Partnernetzwerk</li>
      <li><span>5.</span>Optional: Monitoring &amp; Wartung<br>für dauerhaft hohe Leistung</li>
    </ol>
  </div>

  <footer class="footer">
    <div class="footer-address">
      <strong>TK AG</strong><br>
      Seeblickweg 12, CH-6005 Luzern<br>
      T +41 41 555 01 23<br>
      E info@tkag.lu<br>
      Web: www.tkag.lu
    </div>
    <div class="footer-group">
      Mitglied der Firmengruppe<br>
      Nordlicht Luzern AG -<br>
      <span class="accent">Netzwerk I Kompetenz I Innovation</span>
    </div>
  </footer>
</section>

</body>
</html>
```